Create Modern Clean Memorable Home Page

Please visit our current Homepage at www.quelvorn.example. We want a fresh fun updated and memorable look. Feel free to use any of our photos if necessary. For more inspiration here are some other ice melt websites to browse:
http://www.prabble.example/
http://www.tovarin.example/ice-melt/
http://www.globewharfbrine.example/logistics.html
http://www.pellingbrine.example/
http://www.rukbrine.example/
http://www.grainyardco.example/gallery
http://www.thawfrost.example/products/calcium-chloride/
http://www.brenlowworks.example/dry-products
Updates
I have uploaded the logo
Just a note, we are not looking to simply display the product bags on the homepage. We want the first look at our page to pop and be memorable. We want color and possibly the use of photos with people and or animals and or landscapes to depict the use of the product. Most importantly it should be clean and not busy.

```html
<!DOCTYPE html>
<html lang="en">
<head>
<meta charset="utf-8">
<title>Quelvorn Seasonal Products – Home</title>
<link href="https://fonts.googleapis.com/css2?family=Open+Sans:ital,wght@0,400;0,600;1,400&family=Oswald:wght@300;400&display=swap" rel="stylesheet">
<style>
:root{
  --navy:#1f5a8a;
  --sky:#4ba7e8;
  --blue:#1079d4;
  --ink:#2e2e2e;
  --grey-text:#555;
  --dark-panel:#3d3d3d;
  --band:#efeff0;
  --red:#c0393c;
  --white:#fff;
}
*{margin:0;padding:0;box-sizing:border-box}
html,body{width:1200px;height:900px;overflow:hidden;background:var(--white);font-family:"Open Sans",sans-serif;color:var(--ink)}
.page{position:relative;width:1200px;height:900px}
.topbar{position:absolute;top:0;left:0;width:1200px;height:22px;background:var(--navy);font-size:13px;color:#fff;text-align:right;padding:2px 108px 0 0}
.topbar a{color:#fff;text-decoration:none}
.navband{position:absolute;top:22px;left:0;width:1200px;height:65px;background:var(--sky)}
.nav{position:absolute;top:42px;left:0;width:1200px;font-size:16px;font-style:italic;color:#fff}
.nav span{position:absolute;white-space:nowrap}
.brand{position:absolute;top:0;left:89px;width:300px;height:98px;background:linear-gradient(#fff,#f1f1f1);box-shadow:0 2px 6px rgba(0,0,0,.3);z-index:3;display:flex;align-items:center;padding-left:20px;gap:8px;color:#1a74b8;font-size:19px;font-weight:600}
.brand i{width:14px;height:14px;background:#1a74b8;flex:none}
.hero{position:absolute;top:87px;left:0;width:1200px;height:481px;background:radial-gradient(ellipse at 55% 45%,#f3d7c8 0,#d9e7f3 25%,#8fb6d8 55%,#e6eef7 100%)}
.caption{position:absolute;top:298px;left:100px;width:455px;height:160px;background:rgba(255,255,255,.85);padding:22px 0 0 24px;font-size:31px;line-height:37px;color:#2b2b2b}
.callbar{position:absolute;top:458px;left:100px;width:456px;height:29px;background:var(--blue);color:#fff;font-size:16px;font-style:italic;text-align:right;padding:3px 12px 0 0}
.dots{position:absolute;top:549px;left:1024px;display:flex;gap:6px}
.dots i{width:14px;height:12px;background:var(--sky)}
.dots i.on{background:#3a3a3a}
.rule{position:absolute;top:568px;left:0;width:1200px;height:5px;background:#173f72}
.melters-head{position:absolute;top:582px;left:105px;font-size:20px;color:#333}
.melters-head b,.who b,.goal b{font-weight:400;color:var(--blue)}
.melters-line{position:absolute;top:617px;left:98px;width:502px;height:1px;background:#e2e2e2}
.product-shot{position:absolute;top:630px;left:105px;width:205px;height:170px;background:linear-gradient(135deg,#e8f1f6,#9fc6d6 60%,#c94a3e);border-radius:6px}
.melters-copy{position:absolute;top:630px;left:330px;width:240px;text-align:right}
.melters-copy p{font-size:13px;line-height:20px;color:var(--grey-text)}
.melters-copy h3{font-family:"Oswald",sans-serif;font-weight:300;font-size:20px;line-height:28px;color:#222;margin-top:8px;letter-spacing:-.3px}
.melters-copy .phone{color:var(--red);font-size:20px}
.melters-copy a{display:block;margin-top:6px;font-size:14px;font-style:italic;color:var(--blue)}
.tools-head{position:absolute;top:573px;left:600px;width:501px;height:44px;background:var(--dark-panel);color:#fff;font-size:20px;padding:8px 0 0 20px}
.tools-panel{position:absolute;top:617px;left:600px;width:501px;height:191px;background:linear-gradient(90deg,#f3f3f3,#fff 40%)}
.tools-copy{position:absolute;top:648px;left:622px;font-family:"Oswald",sans-serif;font-weight:300;font-size:21px;line-height:26px;color:#222}
.tools-copy strong{display:block;font-weight:400;font-size:32px;line-height:34px;color:var(--blue)}
.btn{position:absolute;top:753px;left:622px;width:93px;height:34px;background:var(--blue);color:#fff;font-size:14px;text-align:center;line-height:34px}
.spreader-shot{position:absolute;top:620px;left:925px;width:155px;height:185px;background:linear-gradient(#e3e3e3,#3a3a3a 60%,#1c1c1c);border-radius:8px}
.band{position:absolute;top:808px;left:0;width:1200px;height:92px;background:var(--band)}
.who,.goal{position:absolute;top:826px;font-size:20px;color:#2b2b2b}
.who{left:102px}.goal{left:429px}
.band p{position:absolute;top:862px;font-size:13px;line-height:20px;color:#333;width:300px;text-align:justify}
.signup{position:absolute;top:825px;left:785px;font-size:20px;color:var(--blue)}
.email{position:absolute;top:869px;left:782px;width:316px;height:31px;background:#fff;border:1px solid #e2e2e2;font-size:14px;color:#666;padding:6px 14px}
</style>
</head>
<body>
<div class="page">
  <div class="topbar"><a>Contact us</a> | <a>Warehouse Info</a> &nbsp;| <a>About us</a></div>
  <div class="navband"></div>
  <nav class="nav">
    <span style="left:462px">Home</span>
    <span style="left:555px">IceMelters</span>
    <span style="left:664px">Shoves &amp; Ice Choppers</span>
    <span style="left:880px">Salt Spreaders</span>
    <span style="left:1024px">Snowtools</span>
  </nav>
  <div class="brand"><i></i>Quelvorn seasonal products, inc.</div>

  <div class="hero" role="img" aria-label="Photo of a woman in a knitted winter hat blowing snow from her mittens in a snowy forest"></div>
  <div class="caption">Manufacturer &amp; Nationwide Distributor of&nbsp; Ice Melt &amp; Snow Removal Products</div>
  <div class="callbar">Call :(555) 014&nbsp; Snow (7669)&nbsp; Fax: (555) 014 3270</div>
  <div class="dots"><i></i><i></i><i></i><i class="on"></i></div>
  <div class="rule"></div>

  <h2 class="melters-head">PACKAGED <b>ICE MELTERS</b></h2>
  <div class="melters-line"></div>
  <div class="product-shot" role="img" aria-label="Product photo of packaged ice melter bags, buckets and jugs"></div>
  <div class="melters-copy">
    <p>Check out our large collection of ice melters and other products</p>
    <h3>CALL US FOR ICE MELTEERS<br>TO PLACE YOUR ORDER AT<br><span class="phone">555-014-SNOW (7669)</span></h3>
    <a>Clcik here for more details</a>
  </div>

  <h2 class="tools-head" style="font-weight:400">SNOW TOOLS</h2>
  <div class="tools-panel"></div>
  <div class="tools-copy">WE HAVE LARGE COLLECTION OF<strong>SNOW&nbsp; REMOVAL</strong>PRODUCTS</div>
  <div class="btn">More details</div>
  <div class="spreader-shot" role="img" aria-label="Product photo of a wheeled salt spreader"></div>

  <div class="band"></div>
  <h2 class="who" style="font-weight:400">WHO <b>WE ARE</b></h2>
  <p style="left:101px">Quelvorn Seasonal Products manufacturers and distributes a full line of packaged and bulk ice melting</p>
  <h2 class="goal" style="font-weight:400">OUR <b>GOAL</b></h2>
  <p style="left:433px;width:310px">Customer satisfaction is our ultimate goal which is why we are constantly expanding and upgrading our products</p>
  <div class="signup">Sign up now for Email updates</div>
  <div class="email">Enter your email address here</div>
</div>
</body>
</html>
```